Check-up reminder postcard

We require a design for a postcard to remind patients to book their dental check up.

Size: standard postcard 100 x 150mm

We are a small family-focussed dental practice. The design should reflect our brand which is warm & sophisticated as well as incorporate the logo colours. For more information please see our website kellowayfamilydental.com.au.

Target Market(s)

Female aged 30 - 45 years old

Industry/Entity Type

Dental

Requirements
Must have
• The front side should have the copy "We've been missing you...".

Back side of postcard should have area for patient name, address, stamp to be placed. The following copy should be used:

"Dear (please leave space for name)

We've been missing you!

We haven't seen you for your regular dental check up. Please call or visit our website to schedule an appointment. Alternatively, we will be in touch over the next couple of weeks.

We look forward to seeing you again soon!

The Kelloway Family Dental team

Phone: 03 9412 7058 Address: 118 Denholm Road, Kelloway VIC 3152 Web: www.kellowayfamilydental.com.au Email: admin@kellowayfamilydental.com.au"

Include the logo on back side of postcard. Please add the tag line under the logo "Creating beautiful smiles everyday" - sans serif font.

- Design file:
All colours must be converted to CMYK.
Bleed 3mm external from trim.
Trims and registration marks are offset 5mm.
All text to be 3mm from trim if possible.
Nice to have
• Maple leaf as in the logo
Slightly cursive font
Less cluttered look
Should not have
• Cartoons
Pictures of teeth, drills, probes, mirrors
Photos of people

```html
<!DOCTYPE html>
<html lang="en">
<head>
<meta charset="utf-8">
<title>Kelloway Family Dental – Check-up Reminder Postcard</title>
<link href="https://fonts.googleapis.com/css2?family=Marcellus&family=Mulish:wght@400;500&display=swap" rel="stylesheet">
<style>
  :root {
    --teal: #2aa394;
    --slate: #5f6b6e;
    --ink: #1e1e1e;
    --rule: #8a8c88;
    --card-top: #fdfcf8;
    --card-bottom: #f2ebcf;
    --cream-band: #f1e9cd;
    --page: #ffffff;
    --room-light: #e6e1d8;
    --room-mid: #b9ad9c;
    --room-dark: #6e5e4f;
  }
  * { margin: 0; padding: 0; box-sizing: border-box; }
  html, body { width: 1200px; height: 1000px; overflow: hidden; background: var(--page); }
  body { position: relative; font-family: "Mulish", Arial, sans-serif; }

  .postcard {
    position: absolute;
    left: 295px;
    width: 605px;
    height: 404px;
    background: linear-gradient(180deg, var(--card-top) 0%, var(--card-bottom) 100%);
    box-shadow: 3px 4px 8px rgba(0,0,0,0.18);
    overflow: hidden;
  }
  .postcard--front { top: 75px; }
  .postcard--back { top: 518px; }

  .brand-name {
    font-family: "Marcellus", Georgia, serif;
    color: var(--teal);
    font-weight: 400;
    line-height: 1;
    text-align: right;
  }
  .brand-name span { display: block; }

  .postcard--front .brand-name {
    position: absolute;
    right: 20px;
    top: 26px;
    font-size: 31px;
  }
  .postcard--front .brand-name .brand-sub { font-size: 23px; margin-top: 4px; }

  .hero-photo {
    position: absolute;
    left: 0; top: 123px;
    width: 605px; height: 186px;
    background: linear-gradient(90deg, var(--room-mid) 0%, var(--room-light) 30%, var(--room-light) 70%, var(--room-mid) 100%);
  }
  .hero-photo::after {
    content: "";
    position: absolute; left: 0; right: 0; bottom: 0; height: 32%;
    background: linear-gradient(180deg, var(--room-mid), var(--room-dark));
    opacity: 0.55;
  }

  .front-band {
    position: absolute;
    left: 0; top: 309px;
    width: 605px; height: 95px;
    background: var(--cream-band);
  }
  .front-headline {
    position: absolute;
    left: 23px; top: 26px;
    font-family: "Mulish", "Trebuchet MS", sans-serif;
    font-size: 23px;
    letter-spacing: 4.5px;
    color: var(--teal);
    font-weight: 400;
  }

  .postcard--back .brand-block {
    position: absolute;
    right: 304px;
    top: 20px;
    text-align: right;
  }
  .postcard--back .brand-name { font-size: 22px; }
  .postcard--back .brand-name .brand-sub { font-size: 17px; margin-top: 3px; }
  .tagline {
    margin-top: 4px;
    font-size: 9px;
    color: var(--slate);
    letter-spacing: 0.2px;
  }

  .message {
    position: absolute;
    left: 47px; top: 134px;
    width: 225px;
    font-size: 8.6px;
    line-height: 1.22;
    color: var(--ink);
    text-align: justify;
  }
  .message p { margin-bottom: 10px; }
  .message .contact { margin-top: 18px; }

  .divider {
    position: absolute;
    left: 320px; top: 19px;
    width: 2px; height: 332px;
    background: var(--rule);
  }
  .address-lines {
    position: absolute;
    left: 345px; top: 166px;
    width: 223px;
  }
  .address-lines span {
    display: block;
    height: 2px;
    background: var(--rule);
    margin-bottom: 22px;
  }
</style>
</head>
<body>

  <section class="postcard postcard--front" aria-label="Postcard front">
    <div class="brand-name">
      <span>Kelloway</span>
      <span class="brand-sub">Family Dental</span>
    </div>
    <div class="hero-photo" role="img" aria-label="Photo of the practice waiting room with striped armchairs, a sofa and the reception counter"></div>
    <div class="front-band">
      <h1 class="front-headline">We've been missing you...</h1>
    </div>
  </section>

  <section class="postcard postcard--back" aria-label="Postcard back">
    <div class="brand-block">
      <div class="brand-name">
        <span>Kelloway</span>
        <span class="brand-sub">Family Dental</span>
      </div>
      <p class="tagline">Creating beautiful smiles everyday</p>
    </div>

    <div class="message">
      <p>"Dear ..........................................................</p>
      <p>We've been missing you as we haven't seen you for your dental check up.</p>
      <p>Over the next couple of weeks we will be in touch otherwise, please call or visit our website to book an appointment.</p>
      <p>We look forward to seeing you again soon!</p>
      <p>The Kelloway Family Dental team</p>
      <p class="contact">Phone: 03 9412 7058</p>
      <p>Web: www.kellowayfamilydental.com.au"</p>
    </div>

    <div class="divider"></div>
    <div class="address-lines" aria-label="Address lines">
      <span></span><span></span><span></span><span></span>
    </div>
  </section>

</body>
</html>
```